IT recruiter company is looking for a web design
Zielgruppe
We are an IT recruiting company. Our customers are middle to large companies from different branches.
Aufgabenstellung
We need an responsive landing page (home) like those of the competitors like Vorlant (http://vorlant.de) or LORV (http://lorv.de)
The logo is attached as PNG-file. Please let us know if you need an other format.
Would be nice if you can include the colors that are used in the logo into the design

```html
<!DOCTYPE html>
<html lang="de">
<head>
<meta charset="utf-8">
<title>Kenvaro – IT Recruiting</title>
<link href="https://fonts.googleapis.com/css2?family=Montserrat:wght@400;500;600&family=Oswald:wght@400&display=swap" rel="stylesheet">
<style>
  :root {
    --page-bg: #ffffff;
    --nav-text: #56607c;
    --brand: #6a6b92;
    --brand-pill: #6c6f95;
    --hero-blue: #5b86d0;
    --button-blue: #3f74cf;
    --photo-dark: #2f3a55;
    --photo-mid: #7d8aa3;
    --photo-light: #c9d1dd;
    --band-shape: #eceef1;
    --white: #ffffff;
  }
  * { box-sizing: border-box; margin: 0; padding: 0; }
  html, body { width: 1200px; height: 789px; overflow: hidden; background: var(--page-bg); }
  body { font-family: "Montserrat", sans-serif; position: relative; }

  .site-header {
    position: absolute; top: 0; left: 0; width: 1200px; height: 100px;
    background: var(--white);
  }
  .nav-link {
    position: absolute; top: 42px; font-size: 14px; font-weight: 500;
    color: var(--nav-text); letter-spacing: 0.3px; text-transform: uppercase;
  }
  .nav-link--pill {
    top: 37px; background: var(--brand-pill); color: var(--white);
    padding: 5px 8px; font-size: 14px;
  }
  .brand-name {
    position: absolute; left: 500px; top: 20px; font-size: 48px; font-weight: 500;
    color: var(--brand); letter-spacing: -0.5px; line-height: 1;
  }

  .hero {
    position: absolute; top: 100px; left: 0; width: 1200px; height: 600px; overflow: hidden;
  }
  .hero-photo {
    position: absolute; inset: 0;
    background: linear-gradient(115deg, var(--photo-light) 0%, var(--photo-mid) 35%, var(--photo-dark) 55%, var(--photo-mid) 75%, var(--photo-light) 100%);
  }
  .hero-shapes { position: absolute; inset: 0; }
  .hero-content { position: absolute; left: 727px; top: 190px; width: 420px; color: var(--white); }
  .hero-title {
    font-family: "Oswald", sans-serif; font-weight: 400; font-size: 54px; line-height: 56px;
    letter-spacing: 2.5px; text-transform: uppercase;
  }
  .hero-text { margin-top: 18px; font-size: 16px; line-height: 21px; width: 390px; opacity: 0.95; }
  .hero-button {
    display: inline-block; margin-top: 26px; background: var(--button-blue); color: var(--white);
    font-size: 12px; font-weight: 600; letter-spacing: 0.6px; text-transform: uppercase;
    width: 190px; height: 43px; line-height: 43px; text-align: center; text-decoration: none;
  }

  .bottom-band {
    position: absolute; top: 700px; left: 0; width: 1200px; height: 89px; background: var(--white);
  }
</style>
</head>
<body>
  <header class="site-header">
    <nav>
      <a class="nav-link" style="left:85px">Über uns</a>
      <a class="nav-link" style="left:200px">Für Spezialisten</a>
      <a class="nav-link" style="left:366px">Für Kunden</a>
      <span class="brand-name">Kenvaro</span>
      <a class="nav-link nav-link--pill" style="left:743px">My Kenvaro</a>
      <a class="nav-link" style="left:882px">Kontakt</a>
      <a class="nav-link" style="left:995px">Blog</a>
    </nav>
  </header>

  <section class="hero">
    <div class="hero-photo" role="img" aria-label="Businessman in a suit with a briefcase running up a glass office building"></div>
    <svg class="hero-shapes" width="1200" height="600" viewBox="0 0 1200 600">
      <polygon points="680,0 730,0 520,600 470,600" fill="#ffffff" opacity="0.45"/>
      <polygon points="730,0 1200,0 1200,600 520,600" fill="var(--hero-blue)" opacity="0.92"/>
    </svg>
    <div class="hero-content">
      <h1 class="hero-title">Lorem ipsum<br>dolor sit amet</h1>
      <p class="hero-text">In ius diceret reprehendunt. Iisque graecis his cu. Habeo invenire laboramus mel an.</p>
      <a class="hero-button">Jetzt informieren</a>
    </div>
  </section>

  <div class="bottom-band">
    <svg width="1200" height="89" viewBox="0 0 1200 89">
      <polygon points="360,0 470,0 420,45" fill="var(--band-shape)"/>
      <polygon points="480,0 600,0 540,45" fill="var(--band-shape)"/>
    </svg>
  </div>
</body>
</html>
```